New Architectural Firm Business Cards

New Business card to compliment previous pixel forum logo (attached). Please design a business card that is simple, modern, creative....please do not use "symbols", simply the logo and associated graphics/text. The front should contain name/address/phone/email/web address (with graphics).....back should be 100% graphic design using the logo somehow. Hoping for a two color (black and yellow) design. full bleed design, no borders

Target Market(s)

Commercial Architecture Clients

Industry/Entity Type

Architecture

Contact Information for Business Card

Please design a business card that is simple, modern, creative....please do not use "symbols", simply the logo and associated graphics/text. The front should contain name/address/phone/email/web address (with graphics).....back should be 100% graphic design using the logo somehow

Font styles to use
Sans Serif

Colors
FFF300
FFF600
FEFA6F
FFFEC7
FFFEE8

Requirements
Must have
• Clean, Modern Design
Should not have
• Stock images or "icons"

```html
<!DOCTYPE html>
<html lang="en">
<head>
<meta charset="utf-8">
<title>Halden Architecture – Business Card</title>
<link rel="stylesheet" href="https://fonts.googleapis.com/css2?family=Roboto:wght@500&family=Montserrat:wght@500&display=swap">
<style>
  :root {
    --yellow-bright: #FFEC00;
    --yellow-deep: #F7C600;
    --ink: #1c1c1c;
    --paper: #ffffff;
    --page: #ffffff;
  }
  html, body {
    margin: 0;
    padding: 0;
    width: 800px;
    height: 1200px;
    overflow: hidden;
    background: var(--page);
  }
  .canvas {
    position: relative;
    width: 800px;
    height: 1200px;
  }
  .card {
    position: absolute;
    left: 80px;
    width: 640px;
    height: 365px;
    background: var(--paper);
    box-shadow: 0 8px 18px rgba(0,0,0,0.28);
    overflow: hidden;
  }
  .card--logo { top: 205px; }
  .card--contact { top: 630px; }

  .band {
    position: absolute;
    background: linear-gradient(160deg, var(--yellow-bright) 0%, var(--yellow-deep) 100%);
  }
  .band--left { left: 0; top: 0; width: 112px; height: 100%; }
  .band--right { right: 0; top: 0; width: 112px; height: 100%; }
  .band--bottom { left: 0; bottom: 0; width: 100%; height: 73px; }

  .brand {
    position: absolute;
    font-family: "Roboto", sans-serif;
    font-weight: 500;
    color: var(--ink);
    text-align: center;
    line-height: 1.05;
  }
  .brand__dot {
    display: block;
    margin: 0 auto 8px;
    border-radius: 50%;
    background: var(--yellow-deep);
  }
  .card--logo .brand {
    left: 0;
    right: 0;
    top: 95px;
    font-size: 40px;
    letter-spacing: 0.5px;
  }
  .card--logo .brand__dot { width: 60px; height: 60px; margin-bottom: 14px; }
  .card--contact .brand {
    left: 390px;
    width: 222px;
    top: 38px;
    font-size: 24px;
  }
  .card--contact .brand__dot { width: 34px; height: 34px; }

  .holder {
    position: absolute;
    left: 49px;
    top: 40px;
    margin: 0;
    font-family: "Montserrat", sans-serif;
    font-weight: 500;
    font-size: 30px;
    letter-spacing: 0.5px;
    line-height: 1;
    color: var(--ink);
  }
  .holder__first { color: var(--yellow-deep); }

  .contact-list {
    position: absolute;
    left: 51px;
    top: 104px;
    margin: 0;
    padding: 0;
    list-style: none;
    font-family: "Montserrat", sans-serif;
    font-weight: 500;
    font-size: 23px;
    color: var(--ink);
  }
  .contact-list li {
    display: flex;
    align-items: center;
    height: 41px;
  }
  .contact-icon {
    width: 31px;
    height: 31px;
    margin-right: 12px;
    flex: none;
  }
</style>
</head>
<body>
<main class="canvas">

  <section class="card card--logo" aria-label="Card back">
    <div class="band band--left" role="img" aria-label="Yellow geometric border pattern"></div>
    <div class="band band--right" role="img" aria-label="Yellow geometric border pattern"></div>
    <div class="brand">
      <span class="brand__dot"></span>
      HALDEN<br>ARCHITECTURE
    </div>
  </section>

  <section class="card card--contact" aria-label="Card front">
    <div class="band band--bottom" role="img" aria-label="Yellow geometric border pattern"></div>

    <h1 class="holder"><span class="holder__first">YOUR</span> NAME</h1>

    <ul class="contact-list">
      <li>
        <svg class="contact-icon" viewBox="0 0 30 30" aria-hidden="true">
          <circle cx="15" cy="15" r="15" fill="var(--yellow-deep)"/>
          <path d="M10 8 l3 0 l1.5 4 l-2 1.5 q1.5 3.5 4 5 l1.5 -2 l4 1.5 l0 3 q-1 1.5 -3 1.5 q-9 -2 -11 -11 q0 -2 2 -3.5z" fill="#fff"/>
        </svg>
        (123) 456 789 0
      </li>
      <li>
        <svg class="contact-icon" viewBox="0 0 30 30" aria-hidden="true">
          <circle cx="15" cy="15" r="15" fill="var(--yellow-deep)"/>
          <rect x="8" y="10" width="14" height="10" fill="none" stroke="#fff" stroke-width="1.8"/>
          <path d="M8 10 l7 6 l7 -6" fill="none" stroke="#fff" stroke-width="1.8"/>
        </svg>
        your.mail@mail.com
      </li>
      <li>
        <svg class="contact-icon" viewBox="0 0 30 30" aria-hidden="true">
          <circle cx="15" cy="15" r="15" fill="var(--yellow-deep)"/>
          <path d="M7 15 l8 -7 l8 7 M9.5 13.5 v8 h11 v-8" fill="none" stroke="#fff" stroke-width="1.8"/>
          <rect x="13" y="16" width="4" height="5.5" fill="#fff"/>
        </svg>
        No. Street, Country
      </li>
      <li>
        <svg class="contact-icon" viewBox="0 0 30 30" aria-hidden="true">
          <circle cx="15" cy="15" r="15" fill="var(--yellow-deep)"/>
          <circle cx="15" cy="15" r="7" fill="none" stroke="#fff" stroke-width="1.8"/>
          <path d="M8 15 h14 M15 8 q-4 7 0 14 M15 8 q4 7 0 14" fill="none" stroke="#fff" stroke-width="1.4"/>
        </svg>
        www.yourwebsite.com
      </li>
    </ul>

    <div class="brand">
      <span class="brand__dot"></span>
      HALDEN<br>ARCHITECTURE
    </div>
  </section>

</main>
</body>
</html>
```